Dr Fenwick Brochure Plastic Surgeon

We need a three panel brochure for cosmetic surgery designed and ready for print. The brochure will have content and images on both sides. We attached the old brochure. The content needs to stay as on the attached pdf but please feel free to offer new designs. The color needs to match the brochure, which is a light blue and teal. The logo is attached. All images we want on the brochure are also attached.

We are looking for new fresh design but need to keep the content currently on the brochure.
Updates

The tri-fold brochure must be on 8.5" x 11" with an 1/8" bleed for printing.

Target Market(s)

Females ages 25 to 55 yrs old

Industry/Entity Type

Plastic Surgery

Font styles to use
Sans Serif

Colors
34a6d7

Requirements
Must have
• You must use the content provided from the attached brochure. Keep the same content on the current panels. Must use the same color scheme

```html
<!DOCTYPE html>
<html lang="en">
<head>
<meta charset="utf-8">
<title>Helena J. Fenwick, MD – Brochure</title>
<link href="https://fonts.googleapis.com/css2?family=Open+Sans:wght@400;600;700;800&display=swap" rel="stylesheet">
<style>
:root{
  --teal:#1d8a8e;
  --teal-dark:#0d5a5f;
  --teal-light:#4db4b4;
  --teal-band:#3aa3a6;
  --ink:#2b3a3c;
  --paper:#ffffff;
  --bg:#d9dcdd;
}
*{box-sizing:border-box;margin:0;padding:0}
html,body{width:804px;height:1200px;overflow:hidden;background:var(--bg);font-family:"Open Sans",Arial,sans-serif}
.brochure{position:absolute;left:0;top:290px;width:804px;height:621px;display:flex;box-shadow:0 4px 14px rgba(0,0,0,.2)}
.panel{position:relative;width:268px;height:100%;overflow:hidden}
.panel--cosmetic{background:linear-gradient(180deg,#fff,#eef3f3)}
.panel--medical{background:linear-gradient(180deg,#239599,#137379);color:#fff}
.panel--intro{background:var(--paper);width:268px}
.panel-title{height:40px;display:flex;align-items:center;justify-content:center;font-weight:700;font-size:19px;color:#fff;letter-spacing:.3px;background:linear-gradient(90deg,var(--teal),var(--teal-band))}
.panel--medical .panel-title{background:linear-gradient(90deg,#2aa0a3,#45b3b5)}
.site-band{position:absolute;left:0;right:0;bottom:0;height:48px;background:var(--teal-dark);color:#fff;display:flex;align-items:center;justify-content:center;font-size:14px}
.site-band b{font-weight:700}
.pill{display:inline-block;padding:3px 26px 3px 44px;border-radius:0 14px 14px 0;font-size:15px;color:#fff;margin-left:-1px}
.panel--cosmetic .pill{background:var(--teal-light)}
.panel--medical .pill{background:var(--teal-dark);padding-left:40px}
.checklist{list-style:none;margin:8px 0 14px 30px}
.checklist li{position:relative;padding-left:15px;line-height:15.5px}
.checklist li::before{content:"✓";position:absolute;left:0;top:0;font-weight:700}
.panel--cosmetic .checklist{font-size:9.4px;color:#1f2d2e}
.panel--cosmetic .checklist li::before{color:var(--teal-dark)}
.cosmetic-body{padding-top:22px}
.gallery-line{position:absolute;left:20px;bottom:62px;font-size:15px;color:var(--ink)}
.gallery-line b{color:var(--teal);font-weight:700}
.medical-body{padding-top:22px}
.panel--medical .checklist{font-size:12px;margin-left:24px}
.panel--medical .checklist li{line-height:15px;padding-left:17px}
.highlights{text-align:center;font-weight:700;font-size:14px;line-height:18px;margin-top:-2px}
.contact{text-align:center;margin-top:12px;font-size:12px}
.contact svg{display:block;margin:0 auto}
.contact .address{margin-top:4px;line-height:15px}
.contact .cta{font-weight:700;font-size:15px;margin:16px 0 3px}
.contact .phone{font-weight:700;font-size:18px;margin:2px 0 4px}
.contact .email{font-size:11px;margin-top:1px}
.brand{height:86px;display:flex;flex-direction:column;align-items:center;justify-content:center;border-bottom:3px solid var(--teal-light)}
.brand-name{display:flex;align-items:center;gap:6px;font-size:19px;font-weight:600;color:var(--teal-dark);letter-spacing:.5px}
.brand-dot{width:12px;height:12px;border-radius:50%;background:var(--teal-light)}
.brand-sub{font-size:7px;color:var(--teal);text-align:center;line-height:9px;margin-top:3px}
.hero{height:315px;background:radial-gradient(ellipse at 55% 45%,#f1ded3 0%,#d9c6bc 35%,#c7d5dd 70%,#a9c0cc 100%)}
.benefits{list-style:none;padding:22px 10px 0 34px;font-size:13.3px;color:var(--ink)}
.benefits li{position:relative;padding-left:20px;line-height:17px;margin-bottom:5px}
.benefits li::before{content:"✓";position:absolute;left:0;top:0;color:var(--teal-dark);font-weight:700}
</style>
</head>
<body>
<main class="brochure">
  <section class="panel panel--cosmetic">
    <h2 class="panel-title">COSMETIC SERVICES</h2>
    <div class="cosmetic-body">
      <span class="pill">Surgery</span>
      <ul class="checklist">
        <li>C02 Bladeless Incisional Blepharoplasty</li>
        <li>Brow and Forehead Lifts</li>
        <li>Midface Lifts</li>
      </ul>
      <span class="pill">Injectables</span>
      <ul class="checklist">
        <li>Removal of Wrinkles</li>
        <li>Restoration of Facial Volume</li>
        <li>TCA Medium Depth Chemical Peels</li>
        <li>Minimally Invasive Neck Liposuction</li>
        <li>Acne Scar Treatment</li>
        <li>Tighten Neck</li>
        <li>Remove Neck Fullness</li>
      </ul>
      <span class="pill">Lasers</span>
      <ul class="checklist">
        <li>Erase Wrinkles and Fine Lines</li>
        <li>Tighten Skin</li>
        <li>Remove Stretch Marks</li>
        <li>Minimize Vascular Lesions</li>
        <li>Minimize Spider Veins</li>
        <li>Improve Scars</li>
        <li>Remove Skin Tags and Moles</li>
        <li>Remove Dark Spots</li>
        <li>Hair Removal</li>
        <li>Improve Stress Incontinence</li>
        <li>Vaginal Rejuvenation</li>
        <li>Correct Vaginal Dryness and Itching</li>
      </ul>
    </div>
    <p class="gallery-line">See <b>OUR PHOTO GALLERY</b> at</p>
    <footer class="site-band">www.<b>HelenaFenwickMD</b>.com</footer>
  </section>

  <section class="panel panel--medical">
    <h2 class="panel-title">MEDICAL SERVICES</h2>
    <div class="medical-body">
      <span class="pill">Eyelid Surgery</span>
      <ul class="checklist">
        <li>Ptosis</li>
        <li>Trauma</li>
        <li>Tumors</li>
        <li>Upper Blepharoplasty</li>
        <li>Eyelid Malposition</li>
      </ul>
      <span class="pill">Orbital Surgery</span>
      <ul class="checklist">
        <li>Tumors</li>
        <li>Trauma</li>
        <li>Thyroid — Graves Disease</li>
        <li>Enucleation/Evisceration</li>
      </ul>
      <p class="highlights">Tear Duct Surgery<br>Brow &amp; Forehead Lifts<br>Congenital/ Pediatric Disorders</p>
      <div class="contact">
        <svg width="12" height="17" viewBox="0 0 12 17" aria-hidden="true"><path d="M6 0a6 6 0 0 0-6 6c0 4.5 6 11 6 11s6-6.5 6-11a6 6 0 0 0-6-6zm0 8.5A2.5 2.5 0 1 1 6 3.5a2.5 2.5 0 0 1 0 5z" fill="#fff"/></svg>
        <p class="address">584 W. Lakeview Blvd Suite 210<br>Lakeview TX 75010</p>
        <p class="cta">SCHEDULE A CONSULTATION</p>
        <svg width="18" height="18" viewBox="0 0 18 18" aria-hidden="true"><circle cx="9" cy="9" r="8" fill="none" stroke="#fff" stroke-width="1.4"/><path d="M6 5c-.8.6-.9 1.8 0 3.3 1 1.8 2.6 3.4 4.2 4.1 1 .4 1.9.2 2.3-.5l-1.5-1.3-1 .6c-.9-.4-2-1.6-2.4-2.5l.6-1L7 5z" fill="#fff"/></svg>
        <p class="phone">(555) 014-2287</p>
        <svg width="18" height="17" viewBox="0 0 18 17" aria-hidden="true"><rect x="0" y="5" width="4" height="12" fill="#fff"/><rect x="5" y="0" width="9" height="6" fill="#fff"/><rect x="5" y="7" width="13" height="10" fill="#fff"/><g fill="#137379"><rect x="7" y="9" width="2" height="2"/><rect x="11" y="9" width="2" height="2"/><rect x="15" y="9" width="2" height="2"/><rect x="7" y="13" width="2" height="2"/><rect x="11" y="13" width="2" height="2"/><rect x="15" y="13" width="2" height="2"/></g></svg>
        <p class="phone">(555) 016-3390</p>
        <svg width="16" height="11" viewBox="0 0 16 11" aria-hidden="true"><rect x=".5" y=".5" width="15" height="10" fill="none" stroke="#fff"/><path d="M.5.5 8 6l7.5-5.5" fill="none" stroke="#fff"/></svg>
        <p class="email">appointments@helenafenwickmd.com</p>
      </div>
    </div>
    <footer class="site-band">www.<b>HelenaFenwickMD</b>.com</footer>
  </section>

  <section class="panel panel--intro">
    <header class="brand">
      <div class="brand-name"><span>HELENA J. FENWICK, MD</span><span class="brand-dot"></span></div>
      <p class="brand-sub">OCULOFACIAL AESTHETIC &amp; RECONSTRUCTIVE PLASTIC SURGERY<br>COSMETIC LASER SURGERY</p>
    </header>
    <div class="hero" role="img" aria-label="Close-up beauty photograph of a woman's face with a peeling-skin effect and outlined circles marking treatment areas"></div>
    <ul class="benefits">
      <li>Expert in Cosmetic Surgery</li>
      <li>DFWs only Board Certified Cosmetic Laser Surgeon</li>
      <li>Triple Board Certified in Eyelid and Facial Plastic Surgery</li>
      <li>Customized Care</li>
      <li>Feminine Approach</li>
    </ul>
    <footer class="site-band">www.<b>HelenaFenwickMD</b>.com</footer>
  </section>
</main>
</body>
</html>
```